Fresh & Clean *NEW* BUSINESS CARD Needed - OPTOMETRY Clinic/Optical

High-tech optometry practice with 3 doctors seeking new business card.  We provide eye exams, sell, designer glasses/contacts/specialty eyewear and treat ocular diseases.  For our business cards, we are seeking fresh, clean, and crisp design as we grow our team (staffing change).  Simply adding doctors is making the card look busy/cluttered.
 Looking for professional, less cluttered look yet still have our logo, doctor names, phone, address, and website....If possible!  :)
Names:
Marcia Trelford, O.D.
Ned Pallister, O.D.
Oona Ferrant, O.D.
Phone: 555-014-2738
Website: www.BrightLensHub.example
Address:  417 Garnet R. Holloway, Maple Hollow, ZZ 00000
Ultimately we have the main business card with all doctor sames and that card has two versions  (front is always the same).  The back has two designs (1) displays next appointment time/date, (2) for "general use" (non-appointment.)    I have attached what we have used in the past.  
We also need a design template for each team member in our practice with their name, title, and email.   Those should be designed with the "general use" back (see attached).
**Open to entirely new design so don't feel obligated to keep current format.  Need new perspective!  Also including our watermark and some other design features we have consistently used in past in our portfolio.  Included are two options for logos--vertical and horizontal.
**I also would like to remove "Member of Sight Alliance" on our logo if possible**
 Other image files available upon request.

Target Market(s)

New patient & Current Patients

Industry/Entity Type

Optometry

Contact Information for Business Card

High-tech optometry practice with 3 doctors seeking new business card.  We provide eye exams, sell, designer glasses/contacts/specialty eyewear and treat ocular diseases.  For our business cards, we are seeking fresh, clean, and crisp design as we grow our team (staffing change).  Simply adding doctors is making the card look busy/cluttered.  Looking for professional, less cluttered look yet still have our logo, doctor names, phone, address, and website....If possible!  :) Names: Marcia Trelford, O.D. Ned Pallister, O.D. Oona Ferrant, O.D. Phone: 555-014-2738 Website: www.BrightLensHub.example Address:  417 Garnet R. Holloway, Maple Hollow, ZZ 00000 Ultimately we have the main business card with all doctor sames and that card has two versions  (front is always the same).  The back has two designs (1) displays next appointment time/date, (2) for "general use" (non-appointment.)    I have attached what we have used in the past.   We also need a design template for each team member in our practice with their name, title, and email.   Those should be designed with the "general use" back (see attached). **Open to entirely new design so don't feel obligated to keep current format.  Need new perspective!  Also including our watermark and some other design features we have consistently used in past in our portfolio.  Included are two options for logos--vertical and horizontal. **I also would like to remove "Member of Sight Alliance" on our logo if possible**  Other image files available upon request.

Font styles to use
Other font styles liked:
• We have used Montserrat / Yellowtail in the past

Colors

Designer to choose colors to be used in the design.

Requirements
Must have
• Clean & Fresh Design with Logo / Info provided in description. Horizontal orientation. **I have included the CMYK colors we currently have in our logo.
Should not have
• Cluttered

```html
<!DOCTYPE html>
<html lang="en">
<head>
<meta charset="utf-8">
<title>Bright Lens Hub – Business Cards</title>
<link href="https://fonts.googleapis.com/css2?family=Montserrat:wght@300;400;700&family=Arimo:wght@400&display=swap" rel="stylesheet">
<style>
  :root {
    --bg: #e6e6e6;
    --slate: #6d6e70;
    --slate-light: #7c7d80;
    --gold: #d4a300;
    --sky: #a9dde6;
    --paper: #ffffff;
    --ink: #5a5b5d;
    --rule: #8a8a8a;
    --ghost: #ececec;
  }
  * { margin: 0; padding: 0; box-sizing: border-box; }
  html, body { width: 1200px; height: 900px; overflow: hidden; }
  body { background: var(--bg); position: relative; font-family: "Arimo", Arial, sans-serif; }

  .card {
    position: absolute;
    width: 520px;
    height: 300px;
    overflow: hidden;
    background: var(--paper);
    box-shadow: 0 14px 22px rgba(0,0,0,0.28);
  }
  .card--front { left: 340px; top: 90px; }
  .card--back { left: 50px; top: 500px; background: linear-gradient(180deg, var(--slate-light), var(--slate)); }
  .card--appointment { left: 630px; top: 500px; }

  .front-shape { position: absolute; inset: 0; }

  .doctor-list {
    position: absolute; left: 25px; top: 70px;
    font-family: "Montserrat", sans-serif; font-weight: 700;
    font-size: 14.5px; line-height: 18px; color: var(--gold);
  }
  .address {
    position: absolute; left: 25px; top: 152px;
    font-style: normal;
    font-size: 12.5px; line-height: 16px; color: var(--paper);
  }
  .contact {
    position: absolute; left: 25px; top: 199px;
    font-size: 12.5px; line-height: 16px; color: var(--paper);
    list-style: none;
  }
  .contact li { display: flex; align-items: center; gap: 8px; }
  .contact svg { width: 11px; height: 11px; flex: none; }

  .brand-stack {
    position: absolute; left: 300px; top: 66px; width: 200px;
    display: flex; flex-direction: column; align-items: center;
  }
  .brand-dot { width: 64px; height: 64px; border-radius: 50%; background: var(--sky); margin-bottom: 16px; }
  .brand-name {
    font-family: "Montserrat", sans-serif; font-weight: 300;
    color: var(--ink); font-size: 35px; line-height: 39px; text-align: center; letter-spacing: 0.5px;
  }

  .back-brand {
    position: absolute; left: 0; right: 0; top: 46px;
    display: flex; flex-direction: column; align-items: center;
  }
  .back-brand .brand-dot { width: 100px; height: 100px; margin-bottom: 16px; }
  .back-brand .brand-name { color: var(--paper); font-size: 32px; line-height: 36px; }
  .back-web {
    position: absolute; left: 0; right: 0; top: 258px; text-align: center;
    color: var(--paper); font-size: 13px;
  }

  .appt-title {
    position: absolute; left: 34px; top: 33px;
    font-size: 20.5px; font-weight: 400; color: var(--ink);
  }
  .appt-brand {
    position: absolute; right: 36px; top: 38px;
    display: flex; align-items: center; gap: 6px;
    font-family: "Montserrat", sans-serif; font-weight: 400; font-size: 11px;
    color: var(--ink); letter-spacing: 0.5px;
  }
  .appt-brand .brand-dot { width: 14px; height: 14px; margin: 0; }
  .appt-ghost {
    position: absolute; left: 160px; width: 210px; top: 118px; text-align: center;
    font-family: "Montserrat", sans-serif; font-weight: 300; font-size: 40px; line-height: 44px;
    color: var(--ghost);
  }
  .appt-lines { position: absolute; left: 34px; right: 36px; top: 98px; }
  .appt-lines span { display: block; height: 32px; border-top: 1px dotted var(--rule); }
  .appt-note {
    position: absolute; left: 0; right: 0; top: 254px; text-align: center;
    font-size: 10px; line-height: 13px; color: var(--ink);
  }
</style>
</head>
<body>

<section class="card card--front" aria-label="Business card front">
  <svg class="front-shape" viewBox="0 0 520 300" preserveAspectRatio="none" aria-hidden="true">
    <path d="M0,0 H148 C320,40 320,260 167,300 H0 Z" fill="var(--gold)"/>
    <path d="M0,0 H142 C300,40 300,260 161,300 H0 Z" fill="var(--slate)"/>
  </svg>
  <div class="doctor-list">
    <p>Marcia Trelford, O.D.</p>
    <p>Ned Pallister, O.D.</p>
    <p>Oona Ferrant, O.D.</p>
  </div>
  <address class="address">
    417 Garnet R. Holloway<br>Maple Hollow, ZZ 00000
  </address>
  <ul class="contact">
    <li>
      <svg viewBox="0 0 12 12" aria-hidden="true"><path d="M2.5 0.8 L4.4 2.9 L3.4 4.3 C4.1 5.9 5.6 7.5 7.4 8.4 L8.9 7.4 L11.2 9.3 L9.8 11.2 C5 11 0.9 6.4 0.8 2.2 Z" fill="var(--gold)"/></svg>
      555-014-2738
    </li>
    <li>
      <svg viewBox="0 0 12 12" aria-hidden="true"><circle cx="6" cy="6" r="5.5" fill="var(--gold)"/><path d="M3 3.5 C4.5 3 5 4.5 4 5.5 C3.5 6.5 5 7 5 8.5 M8 2.5 C7 4 8.5 5 9.5 5" stroke="var(--slate)" stroke-width="1" fill="none"/></svg>
      BrightLensHub.example
    </li>
  </ul>
  <div class="brand-stack">
    <div class="brand-dot"></div>
    <p class="brand-name">bright lens<br>hub</p>
  </div>
</section>

<section class="card card--back" aria-label="Business card back, general use">
  <div class="back-brand">
    <div class="brand-dot"></div>
    <p class="brand-name">bright lens hub</p>
  </div>
  <p class="back-web">www.BrightLensHub.example</p>
</section>

<section class="card card--appointment" aria-label="Business card back, appointment">
  <p class="appt-ghost" aria-hidden="true">bright lens hub</p>
  <h2 class="appt-title">Next Appointment</h2>
  <div class="appt-brand"><span class="brand-dot"></span>brightlenshub</div>
  <div class="appt-lines" aria-hidden="true"><span></span><span></span><span></span><span></span><span></span></div>
  <p class="appt-note">Please give me 24 hours notice if you are unable to keep your appointment or<br>a cancellation fee may be charged.</p>
</section>

</body>
</html>
```